Introduction:
We are an Australia-based Cyber Security Penetration testing company seeking a website redesign to showcase our services, expertise, and experience. Our target audience includes businesses and organizations of all sizes who are seeking to secure their IT infrastructure against cyber threats. The purpose of the website redesign is to increase our online presence, generate leads, and establish our company as a trusted authority in the industry.
Objectives:
Create a professional and modern website that is easy to navigate and user-friendly.
Provide information about our company, services, and expertise.
Clearly display table of our 3 services: Bug Bounty as a Service, Penetration Testing and Code Review.
Generate leads through online contact forms and calls-to-action.
Optimize the website for search engines to increase visibility and traffic.
Website similar to: https://www.velmoro.com.au/.
Target Audience:
Our target audience includes businesses and organizations of all sizes that require cybersecurity penetration testing services. These include:
Small and medium-sized enterprises (SMEs)
Australian Government agencies
Design Requirements:
Clean, modern, and professional design.
Use of colors that convey trust, reliability, and expertise (such as orange and grey).
Calls-to-action that encourage visitors to contact us or request a quote.
Integration with social media channels to increase engagement and brand awareness.
A blog section to showcase our thought leadership and expertise.
A news section to share updates about our company and the industry.
Content Requirements:
Home page that introduces our company and services and highlights our expertise.
About Us page that provides information about our company, team, and values.
Services page that lists our services and explains the benefits of each.
Case Studies page that showcases our previous work and success stories.
Contact Us page that includes a contact form, phone number, and email address.
Blog section with articles related to the cybersecurity industry and our services.
News section with updates about our company and the industry.

```html
<!DOCTYPE html>
<html lang="en">
<head>
<meta charset="utf-8">
<title>Cindral — Cyber Security</title>
<link href="https://fonts.googleapis.com/css2?family=Plus+Jakarta+Sans:wght@400;500;600;700;800&display=swap" rel="stylesheet">
<style>
:root{
  --orange:#f26b3a;
  --orange-soft:#fde3d9;
  --ink:#1d1d1f;
  --text:#555a60;
  --grey-bg:#f0f1f4;
  --dark:#3e3e40;
  --dark-card:#535355;
  --footer:#2e2e30;
  --white:#ffffff;
  --line:#e3e4e8;
}
*{box-sizing:border-box;margin:0;padding:0}
html,body{width:1200px;height:5035px;overflow:hidden}
body{font-family:"Plus Jakarta Sans",sans-serif;color:var(--ink);background:var(--white);position:relative}
.section{position:absolute;left:0;width:1200px}
.wrap{position:absolute;left:92px;width:1016px;top:0;bottom:0}
.eyebrow{font-size:16px;font-weight:600;color:var(--orange);text-transform:uppercase;letter-spacing:.2px}
.heading{font-size:46px;font-weight:700;line-height:54px;color:var(--ink)}
.rule{width:32px;height:3px;background:var(--orange);margin-top:22px}
.btn{display:inline-flex;align-items:center;gap:8px;background:var(--orange);color:var(--white);font-size:15px;font-weight:600;border-radius:3px;padding:0 24px;height:50px}
.btn svg{width:14px;height:14px}
.ph{display:block}

/* top bar */
.topbar{top:0;height:49px;background:var(--orange);color:var(--white);font-size:15px}
.topbar .wrap{display:flex;align-items:center;justify-content:space-between}
.topbar .item{display:flex;align-items:center;gap:8px}
.topbar .right{display:flex;align-items:center;gap:20px}
.topbar .sep{width:1px;height:20px;background:rgba(255,255,255,.6);margin:0 24px}
.topbar .soc{width:13px;height:13px;border-radius:50%;background:var(--white)}

/* header */
.header{top:49px;height:113px;background:var(--white)}
.header .wrap{display:flex;align-items:center;justify-content:space-between}
.brand{display:flex;align-items:center;gap:10px;font-size:32px;font-weight:700;color:var(--ink)}
.brand .dot{width:26px;height:26px;border-radius:50%;background:var(--orange)}
.nav{display:flex;gap:48px;font-size:16px;font-weight:600}
.nav .active{color:var(--orange)}

/* hero */
.hero{top:162px;height:626px;background:linear-gradient(100deg,#0f1a24 0%,#1d2c3a 45%,#3a4855 70%,#8e9aa5 100%)}
.hero .photo{position:absolute;inset:0}
.hero .copy{position:absolute;left:92px;top:165px;color:var(--white)}
.hero h1{font-size:40px;font-weight:700;line-height:60px}
.hero p{font-size:15.5px;line-height:30px;margin-top:20px;width:490px}
.hero .btn{margin-top:30px}
.hero .slider{position:absolute;left:540px;top:565px;display:flex;align-items:center;gap:16px}
.hero .slider i{width:9px;height:9px;border-radius:50%;background:rgba(255,255,255,.6)}
.hero .slider i.on{background:var(--orange)}

/* welcome */
.welcome{top:788px;height:590px}
.welcome .eyebrow{position:absolute;top:115px}
.welcome .heading{position:absolute;top:150px}
.welcome .rule{position:absolute;top:218px;margin:0}
.welcome p{position:absolute;top:255px;width:460px;font-size:15.5px;line-height:30px;color:var(--text)}
.welcome .btn{position:absolute;top:418px}
.welcome .pic-a{position:absolute;left:611px;top:64px;width:165px;height:119px;background:linear-gradient(135deg,#3b0d14,#7a1622 55%,#1c2e4a)}
.welcome .pic-b{position:absolute;left:721px;top:119px;width:293px;height:349px;background:linear-gradient(160deg,#05141d,#0d3a4a 55%,#2a8a9e 80%,#0b1820)}
.welcome .pic-c{position:absolute;left:539px;top:269px;width:166px;height:199px;background:linear-gradient(150deg,#0c1526,#233b63 60%,#0b1220)}
.scroll{position:absolute;left:556px;top:1334px;width:88px;height:88px;border-radius:50%;background:var(--white);z-index:2}

/* services */
.services{top:1378px;height:777px;background:var(--grey-bg)}
.services .eyebrow{position:absolute;top:117px}
.services .heading{position:absolute;top:148px}
.services .rule{position:absolute;top:267px;margin:0}
.services .intro{position:absolute;left:492px;top:110px;width:524px;font-size:15px;line-height:30px;color:var(--text)}
.cards{position:absolute;top:306px;left:0;display:flex;gap:29px}
.svc{width:319px;height:348px;background:var(--white);box-shadow:0 6px 18px rgba(0,0,0,.06)}
.svc .ph{height:272px}
.svc .foot{height:76px;display:flex;align-items:center;justify-content:space-between;padding:0 16px}
.svc h3{font-size:17.5px;font-weight:700}
.svc .go{width:46px;height:46px;background:var(--orange-soft);color:var(--orange);display:flex;align-items:center;justify-content:center;border-radius:3px}
.svc .go svg{width:15px;height:15px}

/* case studies */
.cases{top:2155px;height:948px;background:var(--dark);color:var(--white)}
.cases .eyebrow{position:absolute;top:113px}
.cases .heading{position:absolute;top:144px;color:var(--white);line-height:61px}
.cases .rule{position:absolute;top:276px;margin:0}
.cases .intro{position:absolute;left:541px;top:113px;width:475px;font-size:15px;line-height:30px;color:#e6e6e8}
.case-row{position:absolute;top:348px;left:0;display:flex;gap:30px}
.case{width:318px;height:481px;background:var(--dark-card)}
.case .ph{height:227px}
.case .body{padding:22px 24px}
.case h3{font-size:18px;font-weight:700}
.case .rule{position:static;margin-top:14px;width:24px}
.case p{font-size:14.5px;line-height:28.5px;color:#e4e4e6;margin-top:16px}
.case .btn{margin-top:18px;height:50px;padding:0 26px}

/* contact */
.contact{top:3103px;height:668px;background:radial-gradient(ellipse at 0% 50%,#fbe2d7 0%,rgba(255,255,255,0) 35%),radial-gradient(ellipse at 100% 50%,#fbe2d7 0%,rgba(255,255,255,0) 35%),var(--white)}
.contact .center{position:absolute;left:0;right:0;text-align:center}
.contact .eyebrow{top:127px}
.contact .heading{top:164px}
.contact .rule.center{left:584px;right:auto;top:227px;margin:0}
.form{position:absolute;left:172px;top:266px;width:856px}
.form .row{display:flex;gap:17px}
.field{flex:1;height:47px;background:var(--grey-bg);font-size:15px;color:var(--text);padding:0 16px;display:flex;align-items:center}
.field.msg{margin-top:23px;height:117px;align-items:flex-start;padding-top:22px}
.form .btn{position:absolute;left:340px;top:221px;height:48px;width:176px;justify-content:center;padding:0}

/* blogs */
.blogs{top:3771px;height:796px;background:var(--grey-bg)}
.blogs .eyebrow{position:absolute;top:127px}
.blogs .heading{position:absolute;top:158px}
.blogs .rule{position:absolute;top:227px;margin:0}
.blogs .view{position:absolute;right:0;top:148px;height:49px;width:168px;justify-content:center;padding:0}
.blog-row{position:absolute;top:266px;left:0;display:flex;gap:32px}
.post{width:318px;height:410px;background:var(--white);border:1.5px solid #dcdde1;position:relative}
.post .ph{margin:4px;height:190px}
.post .date{position:absolute;left:22px;top:158px;width:58px;height:62px;background:var(--orange);color:var(--white);font-size:15px;font-weight:600;line-height:22px;padding:9px 0 0 6px}
.post h3{font-size:18px;font-weight:700;line-height:29px;padding:34px 20px 0}
.post .rule{margin:16px 0 0 20px;width:24px}
.post .more{display:inline-flex;align-items:center;gap:8px;margin:30px 0 0 20px;background:var(--orange-soft);color:var(--orange);height:50px;width:176px;justify-content:center;font-size:15px;font-weight:600;border-radius:3px}
.post .more svg{width:14px;height:14px}

/* footer */
.footer{top:4567px;height:468px;background:var(--footer);color:#c9c9cc}
.footer .brand{position:absolute;top:140px;color:var(--orange);font-size:32px}
.footer .socials{position:absolute;top:258px;left:16px;display:flex;gap:14px}
.footer .socials i{width:30px;height:30px;border-radius:50%;background:#6a6a6d}
.fcol{position:absolute;top:122px}
.fcol h4{font-size:18px;font-weight:700;color:var(--white)}
.fcol .rule{width:26px;margin-top:14px}
.fcol ul{list-style:none;margin-top:20px;font-size:15px;line-height:37px}
.fcol .ci{display:flex;gap:12px;align-items:flex-start;line-height:26px;margin-bottom:12px}
.fcol .ci svg{width:15px;height:15px;margin-top:5px;flex:none}
.news{position:absolute;left:744px;top:198px;width:272px}
.news .input{display:flex;align-items:center;gap:12px;font-size:15px;height:40px;border-bottom:1px solid #8a8a8d;padding-left:2px}
.news .input svg{width:16px;height:16px}
.news .btn{margin-top:26px;width:272px;justify-content:center;height:51px;padding:0}
.copy{position:absolute;left:0;right:0;top:424px;text-align:center;font-size:14px;color:#77777a}
.copy b{color:var(--orange);font-weight:600}
</style>
</head>
<body>

<svg width="0" height="0" style="position:absolute">
  <defs>
    <symbol id="arrow" viewBox="0 0 16 16"><path d="M2 8h11M9 4l4 4-4 4" fill="none" stroke="currentColor" stroke-width="1.8" stroke-linecap="round" stroke-linejoin="round"/></symbol>
    <symbol id="mail" viewBox="0 0 16 16"><rect x="1.5" y="3" width="13" height="10" rx="1.5" fill="none" stroke="currentColor" stroke-width="1.4"/><path d="M2 4l6 5 6-5" fill="none" stroke="currentColor" stroke-width="1.4"/></symbol>
    <symbol id="phone" viewBox="0 0 16 16"><path d="M4 1.8l2.2 3-1.3 1.6c.8 1.8 2.2 3.2 4 4l1.6-1.3 3 2.2-1 2.2c-5.6-.2-10.3-4.9-10.5-10.5z" fill="none" stroke="currentColor" stroke-width="1.4" stroke-linejoin="round"/></symbol>
    <symbol id="pin" viewBox="0 0 16 16"><path d="M8 15s5-5 5-8.6A5 5 0 0 0 3 6.4C3 10 8 15 8 15z" fill="currentColor"/><circle cx="8" cy="6.4" r="1.8" fill="#2e2e30"/></symbol>
  </defs>
</svg>

<!-- top bar -->
<div class="section topbar">
  <div class="wrap">
    <div class="item"><svg width="16" height="16"><use href="#mail"/></svg>hello@cindral.com.au</div>
    <div class="right">
      <div class="item"><svg width="16" height="16"><use href="#phone"/></svg><b>1800 555 019</b></div>
      <span class="sep"></span>
      <i class="soc"></i><i class="soc"></i><i class="soc"></i><i class="soc"></i>
    </div>
  </div>
</div>

<!-- header -->
<header class="section header">
  <div class="wrap">
    <div class="brand"><span class="dot"></span>Cindral</div>
    <nav class="nav">
      <span class="active">Home</span><span>About Us</span><span>Services</span><span>Case Studies</span><span>Contact Us</span>
    </nav>
  </div>
</header>

<!-- hero -->
<section class="section hero">
  <div class="photo" role="img" aria-label="Smiling IT consultant holding a laptop in a dim server room"></div>
  <div class="copy">
    <h1>Secure their IT infrastructure<br>Against Cyber threats</h1>
    <p>Lorem ipsum dolor sit amet, consectetur adipiscing elit, sed do eiusmod tempor incididunt ut labore et dolore magna aliqua.</p>
    <span class="btn">Get Started Now <svg><use href="#arrow"/></svg></span>
  </div>
  <div class="slider">
    <svg width="16" height="24" viewBox="0 0 16 24"><path d="M12 2L3 12l9 10" fill="none" stroke="#fff" stroke-width="2"/></svg>
    <i class="on"></i><i></i><i></i>
    <svg width="16" height="24" viewBox="0 0 16 24"><path d="M4 2l9 10-9 10" fill="none" stroke="#fff" stroke-width="2"/></svg>
  </div>
</section>

<!-- welcome -->
<section class="section welcome">
  <div class="wrap">
    <div class="eyebrow">Welcome to</div>
    <h2 class="heading">Cindral</h2>
    <div class="rule"></div>
    <p>Lorem ipsum dolor sit amet, consectetur adipiscing elit, sed do eiusmod tempor incididunt ut labore et dolore magna aliqua. Quis ipsum suspisse ultrices gravida. Risus commodo viverra maecenas accumsan lacus vel facilisis.</p>
    <span class="btn">Read More <svg><use href="#arrow"/></svg></span>
    <div class="pic-a ph" role="img" aria-label="Hooded analyst lit in red at a screen"></div>
    <div class="pic-b ph" role="img" aria-label="Finger touching a glowing digital fingerprint interface"></div>
    <div class="pic-c ph" role="img" aria-label="Engineer working at a computer in a dark office"></div>
  </div>
</section>

<div class="scroll">
  <svg width="88" height="88" viewBox="0 0 88 88">
    <defs><path id="ring" d="M44 44m-28 0a28 28 0 1 1 56 0a28 28 0 1 1 -56 0"/></defs>
    <text font-size="8" font-weight="600" letter-spacing="3" fill="#1d1d1f" font-family="Plus Jakarta Sans, sans-serif"><textPath href="#ring">SCROLL DOWN • SCROLL DOWN •</textPath></text>
    <path d="M44 33v22M38 49l6 6 6-6" fill="none" stroke="#1d1d1f" stroke-width="1.6"/>
  </svg>
</div>

<!-- services -->
<section class="section services">
  <div class="wrap">
    <div class="eyebrow">Our Services</div>
    <h2 class="heading">Cyber Security<br>Solutions</h2>
    <div class="rule"></div>
    <p class="intro">Lorem ipsum dolor sit amet, consectetur adipiscing , sed do eiusmod tempor incididunt ut labore et dolore maa aliqua. Quis ipsum suspisse ultrices gravida.</p>
    <div class="cards">
      <article class="svc">
        <div class="ph" role="img" aria-label="Hooded hacker at a laptop in blue and pink light" style="background:linear-gradient(160deg,#1a2a6a,#3a2a8a 50%,#b0285e)"></div>
        <div class="foot"><h3>Bug Bounty as a Service</h3><span class="go"><svg><use href="#arrow"/></svg></span></div>
      </article>
      <article class="svc">
        <div class="ph" role="img" aria-label="Tester pointing at code on a glowing monitor" style="background:linear-gradient(150deg,#06264a,#0b5aa8 55%,#36b2e8)"></div>
        <div class="foot"><h3>Penetration Testing</h3><span class="go"><svg><use href="#arrow"/></svg></span></div>
      </article>
      <article class="svc">
        <div class="ph" role="img" aria-label="Developer in a hoodie reviewing code on a monitor" style="background:linear-gradient(150deg,#2a2320,#4a3a32 50%,#1a1a1c)"></div>
        <div class="foot"><h3>Code Review</h3><span class="go"><svg><use href="#arrow"/></svg></span></div>
      </article>
    </div>
  </div>
</section>

<!-- case studies -->
<section class="section cases">
  <div class="wrap">
    <div class="eyebrow">Case Studies</div>
    <h2 class="heading">Our Previous work<br>and Success Stories</h2>
    <div class="rule"></div>
    <p class="intro">Etiam tempus, lorem at semper congue, urna turpis mattis metus, ut sodales nibh tellus non massa. Nam at posuere enim. Praesent et dictum augue, in suscipit mauris.</p>
    <div class="case-row">
      <article class="case">
        <div class="ph" role="img" aria-label="Two colleagues reviewing work at a desktop computer" style="background:linear-gradient(150deg,#2d3440,#5a6674 55%,#2a2f36)"></div>
        <div class="body"><h3>Phasellus facilisis ipsum</h3><div class="rule"></div><p>Phasellus dolor leus, condimentum quis consequat sed, porttitor id ex. Aliquam elementum</p><span class="btn">Read More <svg><use href="#arrow"/></svg></span></div>
      </article>
      <article class="case">
        <div class="ph" role="img" aria-label="Woman working alone in a bright open-plan office" style="background:linear-gradient(150deg,#6d6a5e,#a8a696 50%,#3a3a36)"></div>
        <div class="body"><h3>Phasellus facilisis ipsum</h3><div class="rule"></div><p>Phasellus dolor leus, condimentum quis consequat sed, porttitor id ex. Aliquam elementum</p><span class="btn">Read More <svg><use href="#arrow"/></svg></span></div>
      </article>
      <article class="case">
        <div class="ph" role="img" aria-label="Analyst at a desk with several monitors showing data" style="background:linear-gradient(150deg,#1c2a44,#3f5e88 55%,#1a2232)"></div>
        <div class="body"><h3>Phasellus facilisis ipsum</h3><div class="rule"></div><p>Phasellus dolor leus, condimentum quis consequat sed, porttitor id ex. Aliquam elementum</p><span class="btn">Read More <svg><use href="#arrow"/></svg></span></div>
      </article>
    </div>
  </div>
</section>

<!-- contact -->
<section class="section contact">
  <div class="eyebrow center">Contact Us</div>
  <h2 class="heading center">Send us a Message</h2>
  <div class="rule center"></div>
  <div class="form">
    <div class="row"><div class="field">Name</div><div class="field">Email</div><div class="field">Phone</div></div>
    <div class="field msg">Message</div>
    <span class="btn">Submit Now <svg><use href="#arrow"/></svg></span>
  </div>
</section>

<!-- blogs -->
<section class="section blogs">
  <div class="wrap">
    <div class="eyebrow">Latatest News</div>
    <h2 class="heading">Check out our Latest blogs</h2>
    <div class="rule"></div>
    <span class="btn view">View All <svg><use href="#arrow"/></svg></span>
    <div class="blog-row">
      <article class="post">
        <div class="ph" role="img" aria-label="Man in a suit working on a laptop in a dark office" style="background:linear-gradient(150deg,#1d2430,#3c4658 55%,#6b4a2a)"></div>
        <div class="date">Feb 21<br>2023</div>
        <h3>Aliquam sem est, dapibus ac dui ac blandit maximus</h3><div class="rule"></div>
        <span class="more">Read More <svg><use href="#arrow"/></svg></span>
      </article>
      <article class="post">
        <div class="ph" role="img" aria-label="Woman working on a laptop at night" style="background:linear-gradient(150deg,#121a36,#2a3a6e 55%,#a07040)"></div>
        <div class="date">Feb 21<br>2023</div>
        <h3>Aliquam sem est, dapibus ac dui ac blandit maximus</h3><div class="rule"></div>
        <span class="more">Read More <svg><use href="#arrow"/></svg></span>
      </article>
      <article class="post">
        <div class="ph" role="img" aria-label="Man typing on a laptop in a dark room" style="background:linear-gradient(150deg,#0c0f14,#262c36 55%,#4a3c30)"></div>
        <div class="date">Feb 21<br>2023</div>
        <h3>Aliquam sem est, dapibus ac dui ac blandit maximus</h3><div class="rule"></div>
        <span class="more">Read More <svg><use href="#arrow"/></svg></span>
      </article>
    </div>
  </div>
</section>

<!-- footer -->
<footer class="section footer">
  <div class="wrap">
    <div class="brand"><span class="dot"></span>Cindral</div>
    <div class="socials"><i></i><i></i><i></i><i></i></div>
    <div class="fcol" style="left:256px">
      <h4>Contact Info</h4><div class="rule"></div>
      <ul>
        <li class="ci" style="color:#c9c9cc"><svg style="color:var(--orange)"><use href="#pin"/></svg><span>48 Harbour Lane Melbourne,<br>3000, Australia</span></li>
        <li class="ci"><svg style="color:var(--orange)"><use href="#mail"/></svg><span>hello@cindral.com.au</span></li>
        <li class="ci"><svg style="color:var(--orange)"><use href="#phone"/></svg><span>1800 555 019</span></li>
      </ul>
    </div>
    <div class="fcol" style="left:578px">
      <h4>Quick Links</h4><div class="rule"></div>
      <ul><li>Home</li><li>About Us</li><li>Services</li><li>Case Studies</li><li>Contact Us</li></ul>
    </div>
    <div class="news">
      <div class="input"><svg><use href="#mail"/></svg>Email address</div>
      <span class="btn">Subscribe Now <svg><use href="#arrow"/></svg></span>
    </div>
  </div>
  <div class="copy">© 2023 <b>Cindral</b>. All right reserved</div>
</footer>

</body>
</html>
```